Love pets? Create a veterinary business card that aligns with our new revamped website.

Greetings! We are a five-doctor veterinary hospital that seeks your expertise in designing a new business card that harmonizes with our recently revitalized website: www.tqrn.net. The card should feature our logo, the five doctors, operating hours, contact information, and communicate our purpose and personality.

Contact Information for Business Card

TBA

```html
<!DOCTYPE html>
<html lang="en">
<head>
<meta charset="utf-8">
<title>Cedar Hollow Veterinary Hospital – Business Card</title>
<link rel="stylesheet" href="https://fonts.googleapis.com/css2?family=Dancing+Script:wght@500&family=Open+Sans:wght@600;700&family=Roboto:wght@400;700&display=swap">
<style>
  :root {
    --backdrop: #a9a9a9;
    --card-cream: #ece9e4;
    --brand-green: #4a8a3e;
    --divider: rgba(255,255,255,0.45);
    --white: #ffffff;
  }
  * { margin: 0; padding: 0; box-sizing: border-box; }
  html, body { width: 1200px; height: 1000px; overflow: hidden; }
  body { background: var(--backdrop); position: relative; font-family: "Roboto", sans-serif; }

  .card {
    position: absolute; left: 294px; width: 612px; height: 352px;
    border-radius: 28px; overflow: hidden;
  }
  .card--front { top: 118px; background: var(--card-cream); }
  .card--back { top: 551px; background: var(--brand-green); color: var(--white); }

  /* Front */
  .brand-mark {
    position: absolute; left: 0; right: 0; top: 50px;
    display: flex; flex-direction: column; align-items: center;
  }
  .brand-mark__dot { width: 90px; height: 90px; border-radius: 50%; background: var(--brand-green); margin-bottom: 28px; }
  .brand-mark__name {
    font-family: "Open Sans", sans-serif; font-weight: 600; color: var(--brand-green);
    font-size: 40px; line-height: 1.1; text-align: center;
  }
  .brand-mark__name small { display: block; font-size: 20px; letter-spacing: 0.5px; margin-top: 6px; }
  .front-band {
    position: absolute; left: 0; right: 0; bottom: 0; height: 53px; background: var(--brand-green);
    display: flex; align-items: center; justify-content: center; gap: 6px;
    color: var(--white); font-family: "Open Sans", sans-serif; font-weight: 700; font-size: 16px;
  }

  /* Back */
  .back-header { position: absolute; left: 0; right: 0; top: 0; height: 114px; border-bottom: 2px solid var(--divider); }
  .back-brand {
    position: absolute; left: 52px; top: 38px; width: 235px;
    font-family: "Open Sans", sans-serif; font-weight: 600; font-size: 20px; line-height: 1.1; color: var(--white);
  }
  .back-brand small { display: block; font-size: 11px; letter-spacing: 0.5px; margin-top: 3px; }
  .address { position: absolute; left: 336px; width: 200px; top: 53px; text-align: center; font-size: 16px; line-height: 20px; }

  .doctor { position: absolute; left: 44px; width: 240px; top: 152px; text-align: center; }
  .doctor__name { font-family: "Dancing Script", cursive; font-weight: 500; font-size: 46px; line-height: 1; }
  .doctor__title { font-family: "Open Sans", sans-serif; font-weight: 600; font-size: 22px; margin-top: 4px; }

  .hours { position: absolute; left: 306px; width: 260px; top: 166px; text-align: center; font-size: 18px; line-height: 22px; }
  .hours b { font-weight: 700; }

  .phone {
    position: absolute; left: 52px; top: 285px; width: 227px; height: 37px; border-radius: 19px;
    background: var(--white); color: var(--brand-green);
    display: flex; align-items: center; justify-content: center; gap: 6px;
    font-family: "Open Sans", sans-serif; font-weight: 700; font-size: 24px;
  }
  .online { position: absolute; left: 336px; width: 200px; top: 280px; text-align: center;
    font-family: "Open Sans", sans-serif; font-weight: 700; font-size: 18px; line-height: 22px; }
  .online div { display: flex; align-items: center; justify-content: center; gap: 5px; }
</style>
</head>
<body>

<section class="card card--front">
  <div class="brand-mark">
    <div class="brand-mark__dot"></div>
    <div class="brand-mark__name">Cedar Hollow<small>VETERINARY HOSPITAL</small></div>
  </div>
  <div class="front-band">
    <svg width="15" height="15" viewBox="0 0 16 16" fill="none" stroke="#fff" stroke-width="1.4"><circle cx="8" cy="8" r="6.5"/><ellipse cx="8" cy="8" rx="3" ry="6.5"/><path d="M1.5 8h13M2.5 4.8h11M2.5 11.2h11"/></svg>
    www.tqrn.net
  </div>
</section>

<section class="card card--back">
  <header class="back-header">
    <div class="back-brand">Cedar Hollow<small>VETERINARY HOSPITAL</small></div>
    <address class="address" style="font-style:normal">4820 Brookmere Lane<br>Fort Worth, TX 76137</address>
  </header>

  <div class="doctor">
    <div class="doctor__name">Dale Marrow</div>
    <div class="doctor__title">DVM</div>
  </div>

  <div class="hours">
    <div><b>Mon-Fri:</b> 7:00am - 6:00pm</div>
    <div><b>Sat:</b> 8:00am - 12:00pm</div>
    <div><b>Sun:</b> Closed</div>
  </div>

  <div class="phone">
    <svg width="22" height="22" viewBox="0 0 24 24" fill="#4a8a3e"><path d="M6.6 10.8a15.1 15.1 0 0 0 6.6 6.6l2.2-2.2a1 1 0 0 1 1-.25 11.4 11.4 0 0 0 3.6.57 1 1 0 0 1 1 1V20a1 1 0 0 1-1 1A17 17 0 0 1 3 4a1 1 0 0 1 1-1h3.5a1 1 0 0 1 1 1c0 1.25.2 2.45.57 3.57a1 1 0 0 1-.25 1z"/></svg>
    (555) 284-6190
  </div>

  <div class="online">
    <div><svg width="15" height="12" viewBox="0 0 16 12" fill="#fff"><path d="M0 0h16v12H0z"/><path d="M0 0l8 6 8-6" fill="none" stroke="#4a8a3e" stroke-width="1.5"/></svg>info@tqrn.net</div>
    <div><svg width="15" height="15" viewBox="0 0 16 16" fill="none" stroke="#fff" stroke-width="1.4"><circle cx="8" cy="8" r="6.5"/><ellipse cx="8" cy="8" rx="3" ry="6.5"/><path d="M1.5 8h13M2.5 4.8h11M2.5 11.2h11"/></svg>www.tqrn.net</div>
  </div>
</section>

</body>
</html>
```